Life and Personal development life coach needs card design

I need a card design that matches the style and design of my website. I'd like to stay in the same color scheme. Please check out my website for ideas. www.brivelmorcott.com
I have had previous designs for this. I am wondering if you have access to those for more ideas??

```html
<!DOCTYPE html>
<html lang="en">
<head>
<meta charset="utf-8">
<title>Brivel Morcott – Business Card</title>
<link rel="stylesheet" href="https://fonts.googleapis.com/css2?family=Josefin+Sans:wght@300;400;700&family=Josefin+Slab:wght@300;400;600&family=Parisienne&display=swap">
<style>
  :root {
    --backdrop: #e9e9ec;
    --pink-light: #e690c6;
    --pink-mid: #d05aa6;
    --pink-deep: #b23a86;
    --pink-band: #eaa6d0;
    --lime-light: #bcd654;
    --lime-deep: #a6c23a;
    --photo-light: #8d8d8d;
    --photo-dark: #2b2b2b;
    --ink-white: #ffffff;
  }
  * { box-sizing: border-box; margin: 0; padding: 0; }
  html, body {
    width: 1200px; height: 800px; overflow: hidden;
    background: var(--backdrop);
  }
  .sheet {
    width: 1200px; height: 800px;
    display: flex; align-items: center; justify-content: center; gap: 50px;
  }
  .card {
    position: relative; width: 525px; height: 300px; overflow: hidden;
    border-radius: 3px;
    box-shadow: 0 6px 18px rgba(0,0,0,.18);
    color: var(--ink-white);
  }

  /* Contact card (pink) */
  .portrait {
    position: absolute; inset: 0;
    background: radial-gradient(circle at 30% 40%, var(--photo-light), var(--photo-dark) 85%);
  }
  .contact-shape { position: absolute; inset: 0; }
  .contact-details {
    position: absolute; left: 262px; top: 42px; right: 20px;
    font-family: "Josefin Sans", sans-serif;
  }
  .contact-name { font-weight: 700; font-size: 20px; letter-spacing: .3px; line-height: 1; }
  .contact-title {
    font-family: "Josefin Slab", serif; font-size: 10.5px; letter-spacing: .6px;
    text-transform: uppercase; margin-top: 6px;
  }
  .contact-phone {
    display: flex; align-items: center; gap: 6px;
    font-weight: 700; font-size: 21px; margin-top: 24px;
  }
  .contact-phone svg { width: 15px; height: 15px; }
  .contact-line { font-weight: 300; font-size: 14px; margin-top: 10px; }
  .contact-line + .contact-line { margin-top: 6px; }
  .contact-line b { font-weight: 700; }
  .contact-quote {
    font-family: "Josefin Slab", serif; font-size: 15px; margin-top: 14px;
  }

  /* Services card (lime) */
  .services {
    background: linear-gradient(135deg, var(--lime-light), var(--lime-deep));
    padding: 30px 36px 0 46px;
  }
  .services-kicker {
    font-family: "Josefin Slab", serif; font-style: italic; font-weight: 300;
    font-size: 17px; letter-spacing: 1px; margin-left: 60px;
  }
  .services-title {
    font-family: "Josefin Slab", serif; font-weight: 400;
    font-size: 80px; line-height: .9; letter-spacing: 2px; margin-top: 2px;
  }
  .services-focus {
    font-family: "Josefin Sans", sans-serif; font-weight: 300;
    font-size: 14px; margin-left: 56px; margin-top: 2px;
  }
  .services-tagline {
    font-family: "Parisienne", cursive; font-size: 30px; margin-top: 10px;
  }
  .services-web {
    font-family: "Josefin Sans", sans-serif; font-weight: 300;
    font-size: 17px; margin-top: 20px; margin-left: 12px;
  }
  .services-web b { font-weight: 700; }
</style>
</head>
<body>
<main class="sheet">

  <section class="card contact-card">
    <div class="portrait" role="img" aria-label="Black and white portrait photograph of the coach"></div>
    <svg class="contact-shape" viewBox="0 0 525 300" preserveAspectRatio="none" aria-hidden="true">
      <defs>
        <linearGradient id="pinkFill" x1="0" y1="0" x2="1" y2="1">
          <stop offset="0" stop-color="var(--pink-light)"/>
          <stop offset=".5" stop-color="var(--pink-mid)"/>
          <stop offset="1" stop-color="var(--pink-deep)"/>
        </linearGradient>
      </defs>
      <path d="M196 0 Q150 150 214 300 L525 300 L525 0 Z" fill="var(--pink-band)"/>
      <path d="M226 0 Q184 150 242 300 L525 300 L525 0 Z" fill="url(#pinkFill)"/>
    </svg>
    <div class="contact-details">
      <h1 class="contact-name">BRIVEL MORCOTT, RN</h1>
      <p class="contact-title">Transformational Life Coach</p>
      <p class="contact-phone">555-014-2286
        <svg viewBox="0 0 24 24" aria-hidden="true"><path fill="currentColor" d="M6.6 10.8a15.1 15.1 0 0 0 6.6 6.6l2.2-2.2a1 1 0 0 1 1-.25 11.4 11.4 0 0 0 3.6.57 1 1 0 0 1 1 1V20a1 1 0 0 1-1 1A17 17 0 0 1 3 4a1 1 0 0 1 1-1h3.5a1 1 0 0 1 1 1c0 1.25.2 2.45.57 3.57a1 1 0 0 1-.25 1z"/></svg>
      </p>
      <p class="contact-line">brivel@<b>brivelmorcott</b>.com</p>
      <p class="contact-line">www.<b>brivelmorcott</b>.com</p>
      <p class="contact-quote">"Discover what is possible today!"</p>
    </div>
  </section>

  <section class="card services">
    <p class="services-kicker">Transformation and Personal Development</p>
    <h2 class="services-title">LIFE COACH</h2>
    <p class="services-focus">Health, Strength &amp; Balance for Your Mind and Soul</p>
    <p class="services-tagline">Discover a life without limits!</p>
    <p class="services-web">www.<b>brivelmorcott</b>.com</p>
  </section>

</main>
</body>
</html>
```